【 概要 】 当社では、M&A業界に転職を考える求職者向けの転職支援サービスの立ち上げを行っています。 サイト名は「M&A WORK HARBOR」と言い、当社が運営する法律専門職向け転職サイト「LEGAL WORK HARBOR」の姉妹サイトです。 https://legal-work-harbor-example.com/ そのサービス(M&A WORK HARBOR)のLPのファーストビュー部分のデザインを依頼したいと思います。 【コンペ内容】 ワイヤーフレーム(PC)のファーストビュー付近に赤でラインを引いています。 そこまでのデザインでコンペをさせていただきます。 【 依頼内容 】 ・依頼工程:デザインのみ ・作業ボリューム:PC・スマホ1P(コンペはファーストビューのみ) 【 提供素材 】 ・ワイヤー、ラフ案:PCのみあり (添付PDF参照) ・画像:あり (添付画像参照、我々のイメージに近い写真を選定していますが、より良いイメージがあればご提案いただいても構いません。) 【 デザインイメージ 】 ・ターゲットペルソナ:29歳金融業界(大手メガバンク、証券会社)の男性。 ・雰囲気:シンプルでスタイリッシュ、モダンかつ高級感のあるデザイン。 ・参考サイト:https://kvemu-example.co.jp/lp/ 【ロゴについて】 添付します 【その他デザイン参考ページ】 https://legal-work-harbor-example.com/lawyer/lp/steps/ ↑当社の別サービスのデザインです 【 納期 】 2024年2月14日 ※コンペ以外のデザイン部分に関しては、コンペ終了後1〜2週間程度を想定しています。 【 報酬 】 12万円 【 追加依頼 】 HTMLコーディングの追加発注も検討しています。 総額20万くらいでHTMLまで完成させたいと考えていますので、追加8万ほどで発注できればと考えております。 ご検討よろしくお願いします。 HTMLに自信がなければ、その部分のみ他の方に発注も可能です。 ご質問がありましたら、気軽にお問い合わせください。 応募をお待ちしております! |
採用の理由
・修正案のイメージが非常に良かったこと
・コーディングまでの依頼が一気通貫でできること
・ポートフォリオからデザイン力が保証できることが理解できたこと
から採用させていただきます。
引き続きよろしくお願いします!
応募者全員へのお礼・コメント
みなさまからの多くのご提案大変ありがとうございました。
今回採用させていただいた理由として
・こちらの意図をよく理解してデザインに反映してくれたこと(修正案もいただきましたが、さらにクオリティが上がっていました)
ことなどを理由に採用させていただきました。
またご機会がありましたら、何卒よろしくお願いいたします。

```html
<!DOCTYPE html>
<html lang="ja">
<head>
<meta charset="UTF-8">
<title>M&amp;A WORK HARBOR | M&amp;A業界への転職支援</title>
<link rel="stylesheet" href="https://fonts.googleapis.com/css2?family=Montserrat:wght@400;600;700&family=Noto+Sans+JP:wght@400;500;700;900&display=swap">
<style>
  :root {
    --navy: #14254a;
    --gold: #958236;
    --gold-light: #b59f45;
    --section-gray: #9ea1a5;
    --white: #ffffff;
    --ink: #1d2230;
    --field-border: #c9ccd3;
    --required: #b8232f;
  }
  * { box-sizing: border-box; margin: 0; padding: 0; }
  html, body { width: 1200px; height: 1042px; overflow: hidden; }
  body {
    font-family: "Noto Sans JP", sans-serif;
    color: var(--ink);
    background: var(--section-gray);
    position: relative;
  }

  /* Header */
  .site-header {
    position: absolute; left: 0; top: 0; width: 1200px; height: 70px;
    background: var(--white);
  }
  .brand {
    position: absolute; left: 148px; top: 23px;
    font-family: "Montserrat", sans-serif; font-weight: 600;
    font-size: 20px; letter-spacing: 1px; color: var(--navy); white-space: nowrap;
  }
  .tagline {
    position: absolute; left: 430px; top: 27px;
    font-size: 12px; color: var(--ink); letter-spacing: 0.5px; white-space: nowrap;
  }

  /* Hero */
  .hero {
    position: absolute; left: 0; top: 70px; width: 1200px; height: 467px;
    background: linear-gradient(90deg, #6f737a 0%, #9a9da2 60%, #a6a9ad 100%);
  }
  .hero-photo {
    position: absolute; left: 0; top: 0; width: 688px; height: 467px;
    background:
      radial-gradient(ellipse 260px 320px at 150px 300px, rgba(22,30,48,0.85) 0%, rgba(22,30,48,0) 100%),
      linear-gradient(100deg, #2a2e36 0%, #4b5059 28%, #7d8188 62%, #9fa2a6 100%);
  }
  .hero-copy { position: absolute; left: 214px; top: 108px; color: var(--white); }
  .hero-title {
    font-size: 36px; font-weight: 700; line-height: 1.35; letter-spacing: 1px;
    text-shadow: 0 1px 4px rgba(0,0,0,0.3); white-space: nowrap;
  }
  .hero-lead { margin-top: 20px; font-size: 13px; line-height: 1.8; width: 440px; }
  .free-banner {
    position: absolute; left: 764px; top: 8px; white-space: nowrap;
    font-size: 34px; font-weight: 900; font-style: italic; color: var(--white);
    letter-spacing: 2px; line-height: 48px;
  }
  .free-banner .sixty {
    display: inline-block; margin: 0 6px 0 4px;
    color: var(--gold-light); font-size: 44px; font-family: "Montserrat", sans-serif; font-weight: 700;
  }

  /* Form panel */
  .entry-form {
    position: absolute; left: 688px; top: 134px; width: 512px; height: 434px;
    background: var(--navy); color: var(--white);
    padding: 32px 52px 0 52px;
  }
  .form-title { text-align: center; font-size: 19px; font-weight: 700; letter-spacing: 1px; }
  .form-steps { margin-top: 26px; display: flex; height: 32px; background: #c8c4b0; }
  .form-step {
    flex: 1; display: flex; align-items: center; justify-content: center;
    font-size: 12px; color: var(--navy);
  }
  .form-step.is-active { background: var(--gold); color: var(--white); }
  .form-row { display: flex; align-items: center; margin-top: 18px; height: 32px; }
  .form-row:first-of-type { margin-top: 26px; }
  .form-label { width: 100px; font-size: 12px; white-space: nowrap; }
  .required {
    flex: 0 0 32px; height: 20px; background: var(--required); font-size: 10px;
    display: flex; align-items: center; justify-content: center; margin-right: 10px;
  }
  .field {
    flex: 1; height: 32px; background: var(--white); border: 1px solid var(--field-border);
    color: #9a9ea8; font-size: 12px; padding-left: 10px; display: flex; align-items: center;
  }
  .field.short { flex: 0 0 64px; }
  .unit { font-size: 12px; margin: 0 10px; }
  .form-footer { display: flex; align-items: center; margin-top: 30px; }
  .submit {
    margin-left: 112px; width: 100px; height: 36px; background: var(--gold);
    color: var(--white); font-size: 14px; font-weight: 500;
    display: flex; align-items: center; justify-content: center;
  }
  .form-note { margin-left: 14px; font-size: 9px; line-height: 1.5; color: #d4d8e2; width: 150px; }

  /* Interview strip */
  .interview { position: absolute; left: 285px; top: 582px; display: flex; align-items: center; }
  .advisor-photo {
    width: 110px; height: 110px; border-radius: 50%;
    background: radial-gradient(circle at 50% 40%, #d8d9dc 0%, #9da0a6 70%, #6c7077 100%);
    border: 3px solid var(--white);
  }
  .interview-text { margin-left: 20px; font-size: 31px; font-weight: 700; color: var(--ink); letter-spacing: 1px; white-space: nowrap; }
  .badge {
    margin-left: 20px; height: 32px; padding: 0 18px; background: var(--gold);
    color: var(--white); font-size: 13px; font-weight: 500;
    display: flex; align-items: center; white-space: nowrap;
  }

  /* Reasons */
  .reason-bg {
    position: absolute; left: 10px; top: 700px;
    font-family: "Montserrat", sans-serif; font-weight: 400; font-size: 128px;
    letter-spacing: 14px; color: rgba(255,255,255,0.22); line-height: 1;
  }
  .reasons-title {
    position: absolute; left: 0; top: 766px; width: 1200px; text-align: center;
    font-size: 21px; font-weight: 700; letter-spacing: 2px; color: var(--ink);
  }
  .reason-card { position: absolute; top: 830px; width: 274px; }
  .reason-card:nth-of-type(1) { left: 148px; }
  .reason-card:nth-of-type(2) { left: 463px; }
  .reason-card:nth-of-type(3) { left: 778px; }
  .reason-image { width: 274px; height: 82px; }
  .reason-image.agent { background: linear-gradient(135deg, #3a3a3c, #7a7975); }
  .reason-image.consult { background: linear-gradient(135deg, #34353a, #a9a8a3); }
  .reason-image.network { background: linear-gradient(135deg, #5f8fc4, #b9cfe6); }
  .reason-heading { margin-top: 18px; font-size: 18px; font-weight: 700; color: var(--ink); white-space: nowrap; }
  .reason-text { margin-top: 8px; font-size: 11px; line-height: 1.6; color: var(--ink); }
</style>
</head>
<body>
  <header class="site-header">
    <div class="brand">M&amp;A WORK HARBOR</div>
    <p class="tagline">M&amp;A業界の転職に、有能なパートナーを。</p>
  </header>

  <section class="hero">
    <div class="hero-photo" role="img" aria-label="ネクタイを締めるスーツ姿のビジネスマンの写真"></div>
    <div class="hero-copy">
      <h1 class="hero-title">M&amp;A業界への転職には、<br>パートナーが必要だ。</h1>
      <p class="hero-lead">M&amp;A WORK HARBORは、M&amp;A業界を経験した専門のキャリアアドバイザーによる転職支援サービスです。</p>
    </div>
    <p class="free-banner">完全無料 登録<span class="sixty">60</span>秒</p>
  </section>

  <form class="entry-form">
    <h2 class="form-title">M&amp;A専門アドバイザーに相談する</h2>
    <div class="form-steps">
      <span class="form-step is-active">プロフィール</span>
      <span class="form-step">希望条件</span>
      <span class="form-step">登録完了</span>
    </div>
    <div class="form-row"><span class="form-label">お名前</span><span class="required">必須</span><span class="field">例) 佐藤　太郎</span></div>
    <div class="form-row"><span class="form-label">メールアドレス</span><span class="required">必須</span><span class="field">例) taro@example.com</span></div>
    <div class="form-row"><span class="form-label">電話番号</span><span class="required">必須</span><span class="field">例) 090-0000-0000</span></div>
    <div class="form-row"><span class="form-label">生年月日</span><span class="required">必須</span><span class="field short"></span><span class="unit">年</span><span class="field short"></span><span class="unit">月</span><span class="field short"></span><span class="unit">日</span></div>
    <div class="form-footer">
      <span class="submit">次へ</span>
      <p class="form-note">ご入力の個人情報は、転職支援の目的にのみ利用いたします。</p>
    </div>
  </form>

  <section class="interview">
    <div class="advisor-photo" role="img" aria-label="女性キャリアアドバイザーの写真"></div>
    <p class="interview-text">登録1分で、キャリア面談</p>
    <span class="badge">オンライン30分</span>
  </section>

  <section class="reasons">
    <div class="reason-bg" aria-hidden="true">REASON</div>
    <h2 class="reasons-title">M&amp;A WORK HARBORが選ばれる理由</h2>
    <article class="reason-card">
      <div class="reason-image agent" role="img" aria-label="握手するビジネスパーソンの写真"></div>
      <h3 class="reason-heading">エージェント自身がM&amp;Aのプロ</h3>
      <p class="reason-text">エージェント自身がM&amp;A業務を経験しているため、紹介企業の特性を理解し、最適な企業の提案が可能。</p>
    </article>
    <article class="reason-card">
      <div class="reason-image consult" role="img" aria-label="書類を前に面談する様子の写真"></div>
      <h3 class="reason-heading">まずは情報収集に最適</h3>
      <p class="reason-text">即セッティングできるオンラインカウンセリングで、業界知識を深める。</p>
    </article>
    <article class="reason-card">
      <div class="reason-image network" role="img" aria-label="青空に伸びる高層ビル群の写真"></div>
      <h3 class="reason-heading">大手M&amp;A企業と繋がるパイプ</h3>
      <p class="reason-text">紹介先のほとんどは経営者クラスとの独自のパイプを構築済み。選考を戦略的に進めます。</p>
    </article>
  </section>
</body>
</html>
```